New Managed IT company needs a business card

We are an IT management and support company that needs a business card design. I have a logo that I'll provide. Blues and blacks match the logo, but i'm open to anything. I want the card to help people take us seriously, but still have some energy and fun in it. The card should communicate stability and a solid company.

Target Market(s)

Target market includes Owners and Presidents at small businesses of 20 - 100 employees in the Pittsburgh PA area.

Industry/Entity Type

Information Technology

Contact Information for Business Card

i am open to other designs, but i imagine having only the logo on one side and then the logo plus all contact details on the other side.

Requirements
Must have
• Our logo
• Company name is optional if the logo makes it obvious
• A name - Lew Tasker
• A title - President
• A phone number - 724-XXX-XXXX
• A mobile phone number - 724-516-0471
• An email address - ltasker@brightlanetech.com
• a website - brightlanetech.com or www.brightlanetech.com
Nice to have
• some people tell me the logo feels like a superhero theme, some fun with that idea might be good. I'm open to ideas.
Should not have
• stock photos of people or computers - especially old looking stuff.

```html
<!DOCTYPE html>
<html lang="en">
<head>
<meta charset="utf-8">
<title>Brightlane Tech – Business Card</title>
<link href="https://fonts.googleapis.com/css2?family=Open+Sans:wght@400;600;700&display=swap" rel="stylesheet">
<style>
  :root {
    --page-bg: #e9e7e6;
    --card-top: #f4f2f2;
    --blue-light: #12aef0;
    --blue-dark: #0a6fc4;
    --ink: #231f20;
    --white: #ffffff;
    --slate-light: #3b3f44;
    --slate-dark: #15181b;
    --faint: #b9b9bc;
    --logo-blue: #1a8fd8;
  }
  html, body {
    margin: 0;
    width: 1200px;
    height: 900px;
    overflow: hidden;
    background: var(--page-bg);
    font-family: "Open Sans", Arial, sans-serif;
  }
  .canvas { position: relative; width: 1200px; height: 900px; }
  .card {
    position: absolute;
    overflow: hidden;
    box-shadow: 0 6px 18px rgba(0,0,0,0.15);
    background: var(--card-top);
  }
  .card-front { left: 238px; top: 62px; width: 555px; height: 343px; }
  .card-back  { left: 459px; top: 518px; width: 560px; height: 343px; }

  .brand {
    position: absolute;
    display: flex;
    align-items: center;
    gap: 16px;
  }
  .brand-dot {
    width: 84px; height: 84px;
    border-radius: 50%;
    background: var(--logo-blue);
    flex: none;
  }
  .brand-name {
    font-weight: 700;
    font-size: 30px;
    line-height: 1.05;
    letter-spacing: 3px;
    color: var(--ink);
    text-transform: uppercase;
  }
  .card-front .brand { left: 93px; top: 48px; }

  .card-back .brand { left: 95px; top: 51px; opacity: 0.55; }
  .card-back .brand-dot { background: var(--faint); width: 80px; height: 80px; }
  .card-back .brand-name { color: var(--faint); }

  .contact-band {
    position: absolute; left: 0; right: 0; top: 185px; bottom: 0;
    background: linear-gradient(to bottom, var(--blue-light), var(--blue-dark));
    color: var(--white);
  }
  .person {
    position: absolute; right: 338px; top: 55px;
    text-align: right;
  }
  .person-name { font-weight: 700; font-size: 19px; line-height: 24px; }
  .person-title { font-size: 15px; line-height: 20px; }
  .contact-list {
    position: absolute; left: 238px; top: 42px;
    margin: 0; padding: 0; list-style: none;
    font-size: 15px; line-height: 20px;
  }
  .contact-list li { display: flex; align-items: center; gap: 9px; }
  .contact-list svg { width: 12px; height: 12px; fill: var(--white); flex: none; }

  .footer-band {
    position: absolute; left: 0; right: 0; top: 187px; bottom: 0;
    background: linear-gradient(to bottom, var(--slate-light), var(--slate-dark));
    color: var(--white);
    text-align: center;
    font-size: 15px;
    padding-top: 63px;
    box-sizing: border-box;
  }
</style>
</head>
<body>
<div class="canvas">

  <section class="card card-front">
    <div class="brand">
      <span class="brand-dot"></span>
      <span class="brand-name">Brightlane<br>Tech</span>
    </div>
    <div class="contact-band">
      <div class="person">
        <div class="person-name">Lew Tasker</div>
        <div class="person-title">President</div>
      </div>
      <ul class="contact-list">
        <li><svg viewBox="0 0 12 12"><path d="M2.5 0.5l2 2.2-1 1.3c.8 1.7 2 2.9 3.6 3.7l1.3-1 2.2 2-1.2 2.3C5 10.5 1.5 7 0.3 1.7z"/></svg>724-XXX-XXXX</li>
        <li><svg viewBox="0 0 12 12"><path d="M3 0h6v12H3zM4.2 1.2v8.2h3.6V1.2zM5.4 10.2h1.2v1H5.4z"/></svg>724-516-0471</li>
        <li><svg viewBox="0 0 12 12"><path d="M0 2.5h12v7H0zM1 3.3l5 3.4 5-3.4v-.3H1z"/></svg>ltasker@brightlanetech.com</li>
        <li><svg viewBox="0 0 12 12"><circle cx="6" cy="6" r="5.5"/></svg>www.brightlanetech.com</li>
      </ul>
    </div>
  </section>

  <section class="card card-back">
    <div class="brand">
      <span class="brand-dot"></span>
      <span class="brand-name">Brightlane<br>Tech</span>
    </div>
    <div class="footer-band">www.brightlanetech.com</div>
  </section>

</div>
</body>
</html>
```